Roadside building business signage for a holistic health clinic.

Replace signs as shown in the attached file. They are perforated stickers that go on the windows as shown. Looking for something that has our logo and says the name of the practice with logo (Fernbrook Health & Wellness) also boldly says Acupuncture, IV Vitamins, and Holistic Health.
Possibly our phone number as well 538-207-6145

Please don't use pink except the logo. Earthy, organic tone colors appreciated.

Need of eye catching window signage of a holistic clinic on a brick building. Pink, purple, sage green, white color. Logo is pink on a white background. Please don't overload with too much pink. Words to include are "Fernbrook Health and Wellness(name of business)", "Direct Primary Care", " Medical acupuncture", "IV Vitamin Therapy", "fernbrookwholecare-example.com","538-207-6145".

Target Market(s)

People will see in their cars passing by the building. Busy roadside so need to be visible while passing in fast speed.

Industry/Entity Type

Health & Wellness

Font styles to use
Sans Serif

Colors

Designer to choose colors to be used in the design.

Requirements
Must have
• On sign must have words Holistic Medicine, Medical Acupuncture, Direct Primary Care and IV vitamins.
Nice to have
• Simple, minimalistic, artistic yet has clear message. White, Black, Violet, Pink (logo), Dark green, Sage green.
Should not have
• Bold colors (red, yellow, blue), same tone colors. Blue waves on the current signage (uploaded file) must go.

```html
<!DOCTYPE html>
<html lang="en">
<head>
<meta charset="utf-8">
<title>Fernbrook Health &amp; Wellness – Window Signage</title>
<link rel="stylesheet" href="https://fonts.googleapis.com/css2?family=Poppins:wght@500;600;700;800&display=swap">
<style>
  :root {
    --backdrop: #b3b3b3;
    --sign-white: #ffffff;
    --forest: #0f4a3a;
    --ink: #2f2f35;
    --logo-pink: #e0518f;
    --blush: #fdf1f4;
    --sage-line: #cfe8d4;
    --shadow: rgba(0, 0, 0, 0.28);
  }
  * { margin: 0; padding: 0; box-sizing: border-box; }
  html, body { width: 1200px; height: 3294px; overflow: hidden; }
  body {
    background: var(--backdrop);
    font-family: "Poppins", sans-serif;
    position: relative;
  }
  .sign {
    position: absolute;
    background: var(--sign-white);
    box-shadow: 0 4px 14px var(--shadow);
    overflow: hidden;
  }
  .sign--brand { left: 151px; top: 1205px; width: 898px; height: 897px; }
  .sign--services { left: 157px; top: 2198px; width: 886px; height: 886px; }

  .brand-dot {
    position: absolute;
    left: 50%;
    border-radius: 50%;
    background: var(--logo-pink);
    transform: translateX(-50%);
  }
  .sign--brand .brand-dot { top: 190px; width: 210px; height: 210px; }
  .sign--services .brand-dot { top: 56px; width: 136px; height: 136px; }

  .brand-name {
    position: absolute;
    left: 0; right: 0;
    text-align: center;
    color: var(--forest);
    font-weight: 600;
    line-height: 1;
  }
  .brand-name .line { display: block; }
  .sign--brand .brand-name { top: 470px; }
  .sign--brand .brand-name .main { font-size: 98px; letter-spacing: 10px; }
  .sign--brand .brand-name .sub { font-size: 34px; letter-spacing: 10px; margin-top: 22px; }
  .sign--services .brand-name { top: 214px; }
  .sign--services .brand-name .main { font-size: 68px; letter-spacing: 8px; }
  .sign--services .brand-name .sub { font-size: 24px; letter-spacing: 8px; margin-top: 14px; }

  .floral-band {
    position: absolute;
    left: 0; right: 0; bottom: 0;
    height: 216px;
    background: linear-gradient(180deg, var(--blush) 0%, #f4f9f2 100%);
    border-top: 2px solid var(--sage-line);
  }
  .floral-corner {
    position: absolute;
    background: radial-gradient(circle at center, #eef7ee 0%, rgba(238,247,238,0) 70%);
  }
  .floral-corner--top { right: -40px; top: -20px; width: 280px; height: 400px; }
  .floral-corner--bottom { left: -60px; bottom: -20px; width: 240px; height: 360px; }

  .service-list {
    position: absolute;
    left: 110px; top: 368px;
    list-style: none;
  }
  .service {
    display: flex;
    align-items: center;
    height: 80px;
    color: var(--ink);
    font-weight: 700;
    font-size: 44px;
    letter-spacing: -0.5px;
    white-space: nowrap;
  }
  .service svg { width: 56px; height: 56px; margin-right: 28px; flex: none; }

  .website {
    position: absolute;
    left: 0; right: 0; top: 712px;
    text-align: center;
    color: var(--forest);
    font-weight: 600;
    font-size: 30px;
    line-height: 40px;
  }

  .phone-tab {
    position: absolute;
    left: 152px; bottom: 0;
    width: 582px; height: 92px;
    background: var(--forest);
    border-radius: 46px 46px 0 0;
    color: var(--sign-white);
    font-weight: 700;
    font-size: 50px;
    display: flex;
    align-items: center;
    justify-content: center;
    gap: 18px;
  }
  .phone-tab svg { width: 44px; height: 44px; }
</style>
</head>
<body>

  <section class="sign sign--brand" aria-label="Name window sign">
    <div class="brand-dot"></div>
    <h1 class="brand-name">
      <span class="line main">FERNBROOK</span>
      <span class="line sub">HEALTH &amp; WELLNESS</span>
    </h1>
    <div class="floral-band" role="img" aria-label="Soft line-drawn botanical flowers and leaves along the bottom"></div>
  </section>

  <section class="sign sign--services" aria-label="Services window sign">
    <div class="floral-corner floral-corner--top" role="img" aria-label="Faint line-drawn sunflower and leaves in the corner"></div>
    <div class="floral-corner floral-corner--bottom" role="img" aria-label="Faint line-drawn sunflower and leaves in the corner"></div>
    <div class="brand-dot"></div>
    <h2 class="brand-name">
      <span class="line main">FERNBROOK</span>
      <span class="line sub">HEALTH &amp; WELLNESS</span>
    </h2>

    <ul class="service-list">
      <li class="service">
        <svg viewBox="0 0 64 64" aria-hidden="true">
          <rect x="26" y="8" width="12" height="48" rx="2" fill="var(--ink)"/>
          <rect x="8" y="26" width="48" height="12" rx="2" fill="var(--ink)"/>
          <circle cx="32" cy="32" r="5" fill="var(--logo-pink)"/>
        </svg>
        DIRECT PRIMARY CARE
      </li>
      <li class="service">
        <svg viewBox="0 0 64 64" aria-hidden="true">
          <rect x="6" y="40" width="52" height="8" rx="2" fill="var(--ink)"/>
          <rect x="10" y="50" width="4" height="8" fill="var(--ink)"/>
          <rect x="50" y="50" width="4" height="8" fill="var(--ink)"/>
          <circle cx="16" cy="33" r="6" fill="var(--logo-pink)"/>
          <rect x="24" y="29" width="30" height="9" rx="4" fill="var(--logo-pink)"/>
          <line x1="38" y1="8" x2="38" y2="27" stroke="var(--ink)" stroke-width="2.5"/>
          <line x1="46" y1="12" x2="46" y2="27" stroke="var(--ink)" stroke-width="2.5"/>
        </svg>
        MEDICAL ACUPUNCTURE
      </li>
      <li class="service">
        <svg viewBox="0 0 64 64" aria-hidden="true">
          <rect x="10" y="34" width="44" height="20" rx="10" fill="var(--ink)"/>
          <circle cx="32" cy="18" r="9" fill="var(--logo-pink)"/>
        </svg>
        HOLISTIC MEDICINE
      </li>
      <li class="service">
        <svg viewBox="0 0 64 64" aria-hidden="true">
          <rect x="18" y="6" width="28" height="38" rx="6" fill="var(--ink)"/>
          <rect x="24" y="14" width="16" height="18" rx="2" fill="var(--logo-pink)"/>
          <rect x="28" y="44" width="8" height="6" fill="var(--ink)"/>
          <line x1="32" y1="50" x2="32" y2="60" stroke="var(--ink)" stroke-width="2.5"/>
        </svg>
        IV VITAMINS
      </li>
    </ul>

    <p class="website">fernbrookwholecare-example.com</p>

    <div class="phone-tab">
      <svg viewBox="0 0 24 24" aria-hidden="true">
        <path fill="#ffffff" d="M6.6 10.8a15.1 15.1 0 0 0 6.6 6.6l2.2-2.2a1 1 0 0 1 1-.25 11.4 11.4 0 0 0 3.6.57 1 1 0 0 1 1 1V20a1 1 0 0 1-1 1A17 17 0 0 1 3 4a1 1 0 0 1 1-1h3.5a1 1 0 0 1 1 1c0 1.25.2 2.45.57 3.6a1 1 0 0 1-.25 1z"/>
      </svg>
      538-207-6145
    </div>
  </section>

</body>
</html>
```